Comercial & residential carpenter-Property maintanence

Hi, The II at the end of the company (R&T construction II) name is the roman numeral for the number 2 it was the only way i could have that business name, so i was thinking of incorporating the lettering for the business name with the latin alphabet to give some of that old world charm and some how try to show that my work will stand the test of time. Ive also come up with some ideas for slogans, Im not sure if they are any good.
Building the ideas of tomorrow today
Building not just a home but a lifestyle,your lifestyle
If you can dream it we can build it
Not just a home but an extention of you
Building a better tomorrow for today

I work in the building and construction industry in Adelaide South Australia as a carpenter.

Industry/Entity Type

Construction

Contact Information for Business Card

R&T Construction II
Robert Tomas Veld-DuMarais
ABN: 83 472 915 604
BLD: 517 389
PH: 0481 295 713
E Mail: pairmark@mailzone.com.au

```html
<!DOCTYPE html>
<html lang="en">
<head>
<meta charset="utf-8">
<title>R&amp;T Construction II — Business Cards</title>
<link rel="stylesheet" href="https://fonts.googleapis.com/css2?family=Open+Sans:wght@400;600;700&display=swap">
<style>
  :root {
    --backdrop: #c7c8ca;
    --card-white: #f4f4f4;
    --brand-blue: #1f7cc4;
    --blue-light: #2a9be0;
    --blue-deep: #0b7dcc;
    --ink: #2b2b2b;
    --mark-grey: #3f3f41;
    --white: #ffffff;
  }
  * { box-sizing: border-box; margin: 0; padding: 0; }
  html, body {
    width: 1200px; height: 900px; overflow: hidden;
    background: var(--backdrop);
    font-family: "Open Sans", Arial, sans-serif;
  }
  .canvas { position: relative; width: 1200px; height: 900px; }

  .card {
    position: absolute;
    width: 490px; height: 280px;
    left: 355px;
    border-radius: 3px;
    display: flex; flex-direction: column; align-items: center;
    text-align: center;
  }

  /* Contact side */
  .card--contact {
    top: 120px;
    background: var(--card-white);
    padding-top: 40px;
    color: var(--ink);
  }
  .card--contact .brand-name {
    font-size: 24px; font-weight: 600; color: var(--brand-blue);
    letter-spacing: 0.5px; margin-bottom: 24px;
  }
  .person-name { font-size: 16px; font-weight: 700; color: var(--brand-blue); }
  .contact-line { font-size: 13px; line-height: 1.35; }
  .company-name {
    font-size: 16px; font-weight: 700; color: var(--brand-blue);
    margin-top: 14px;
  }
  .registration { font-size: 14px; letter-spacing: 0.3px; }

  /* Brand side */
  .card--brand {
    top: 450px;
    background: linear-gradient(180deg, var(--blue-light) 0%, var(--blue-deep) 100%);
    color: var(--white);
    padding-top: 72px;
  }
  .card--brand .brand-name {
    font-size: 42px; font-weight: 600; letter-spacing: 1px;
  }
  .slogan {
    position: absolute; bottom: 36px; left: 0; right: 0;
    font-size: 15px;
  }
  .slogan strong { font-weight: 700; }

  /* Presentation mark */
  .brand-signoff {
    position: absolute; right: 70px; bottom: 50px;
    font-size: 30px; font-weight: 600; color: var(--mark-grey);
    letter-spacing: 0.5px;
  }
</style>
</head>
<body>
<main class="canvas">
  <section class="card card--contact">
    <p class="brand-name">R&amp;T Construction II</p>
    <p class="person-name">Robert Tomas Veld-DuMarais</p>
    <p class="contact-line">0481 295 713</p>
    <p class="contact-line">pairmark@mailzone.com.au</p>
    <p class="company-name">R&amp;T Construction II</p>
    <p class="registration">ABN: 83 472 915 604 &nbsp;/&nbsp; BLD: 517 389</p>
  </section>

  <section class="card card--brand">
    <p class="brand-name">R&amp;T Construction II</p>
    <p class="slogan">Crafted to last, built around <strong>the way you live!</strong></p>
  </section>

  <p class="brand-signoff">R&amp;T Construction II</p>
</main>
</body>
</html>
```